Hemp (cannabis) CBD Oil 3-page Blog website

The objective is 1) to look like professional/serious company, 2) to get investors excited about our Hemp business, 3) to get investor email and phone numbers and build a sense community. Potential investors should become excited that this is their “window of opportunity,” because VelLorim is made up of extraordinary people who all have made successful business before, that the location in Uruguay is a huge benefit, that we will become the biggest and best CBD-oil manufacturer in Latin America, and that we focus on all-legal medicinal CBD oil extracted from hemp.

Target Market(s)

Potential investors looking to invest between $30,000-$1,000,000 USD into a HEMP startup business, based in Uruguay, South America.

Industry/Entity Type

Business

Number of Pages Required

3 page

Font styles to use
Sans Serif

Requirements
Must have
• Three pages: Home, Members Only, News (blog).
• FOR MORE DETAIL SEE ATTACHED WORD REQUIREMENTS DOCUMENT.
Nice to have
• Uruguay colors: sky blue, golden sun. Medicinal. Legal. Mainstream. Hemp. Professional people. Opportunity/Money/Investor. Uruguay. Latin America. 1st to Market.
Should not have
• Marijuana (HEMP yes, marijuana NO), anything that looks illegal.

```html
<!DOCTYPE html>
<html lang="en">
<head>
<meta charset="utf-8">
<title>VelLorim – CBD-oil manufacturer</title>
<link rel="stylesheet" href="https://fonts.googleapis.com/css2?family=Open+Sans:wght@400;600;700&display=swap">
<style>
:root{
  --orange:#f0a51c;
  --blue:#1d5fb0;
  --green:#7cc142;
  --teal:#3f9a8a;
  --ink:#333333;
  --muted:#6b6b6b;
  --dark:#231f20;
  --white:#ffffff;
  --card:#ececec;
}
*{margin:0;padding:0;box-sizing:border-box}
html,body{width:1200px;height:2590px;overflow:hidden}
body{font-family:"Open Sans",Arial,sans-serif;color:var(--ink);background:var(--white);position:relative}

/* header */
.site-header{position:absolute;left:0;top:0;width:1200px;height:95px;background:var(--white)}
.brand{position:absolute;left:207px;top:38px;display:flex;align-items:center;gap:8px;font-size:28px;font-weight:600;color:var(--blue)}
.brand-dot{width:14px;height:14px;border-radius:50%;background:var(--green)}
.top-contact{position:absolute;right:210px;top:16px;font-size:12px;color:var(--ink);display:flex;gap:22px;align-items:center}
.top-contact svg{vertical-align:-2px;margin-right:5px}
.main-nav{position:absolute;left:432px;top:48px;display:flex;gap:26px;font-size:13px;font-weight:600;align-items:center}
.main-nav a{color:var(--ink);text-decoration:none}
.main-nav a.active{color:var(--green);border-bottom:2px solid var(--green);padding-bottom:3px}
.btn-member{background:var(--blue);color:var(--white)!important;padding:7px 17px;margin-left:2px}

/* hero */
.hero{position:absolute;left:0;top:95px;width:1200px;height:406px;background:linear-gradient(100deg,#6f6a5f 0%,#8c826c 30%,#5d5648 60%,#7a6b50 100%)}
.hero-photo{position:absolute;inset:0;background:radial-gradient(ellipse at 22% 45%,rgba(186,170,60,.55),transparent 45%),radial-gradient(ellipse at 78% 40%,rgba(120,120,70,.6),transparent 40%),linear-gradient(180deg,rgba(0,0,0,.1),rgba(0,0,0,.35))}
.hero-title{position:absolute;left:0;width:1200px;top:138px;text-align:center;font-size:26px;color:var(--white);font-weight:400}
.hero-title span{color:var(--orange)}
.hero-sub{position:absolute;left:320px;width:560px;top:175px;text-align:center;font-size:13px;line-height:1.35;color:var(--white)}
.hero-btn{position:absolute;left:535px;top:233px;width:116px;height:30px;background:var(--orange);color:var(--white);font-size:12px;text-align:center;line-height:30px}
.arrow-btn{position:absolute;width:28px;height:28px;border-radius:50%;display:flex;align-items:center;justify-content:center}

/* headings */
.sec-title{position:absolute;font-size:22px;font-weight:400}
.sec-title .frame{position:absolute;border:5px solid #e6e6e6;width:104px;height:52px;left:34px;top:-16px;z-index:-1}

/* about */
.about-text{position:absolute;left:207px;top:636px;width:325px;font-size:11.5px;line-height:1.48;color:var(--muted)}
.about-text p{margin-bottom:16px}
.btn-orange{position:absolute;background:var(--orange);color:var(--white);font-size:12px;text-align:center}
.process-map{position:absolute;left:622px;top:561px}

/* team */
.team{position:absolute;left:0;top:998px;width:1200px;height:404px;background:var(--dark)}
.team-watermark{position:absolute;left:-10px;top:148px;font-size:92px;font-weight:700;color:rgba(255,255,255,.04);letter-spacing:4px}
.team-title{color:var(--white);left:207px;top:98px}
.team-title .frame{border-color:#4a4647}
.team-text{position:absolute;left:207px;top:166px;width:260px;font-size:11.5px;line-height:1.45;color:#d8d8d8}
.team-rule{position:absolute;left:207px;top:256px;width:88px;height:1px;background:var(--green)}
.member{position:absolute;width:156px;height:148px}
.member-hover{position:absolute;left:6px;top:6px;width:146px;height:142px;background:var(--green);color:var(--white);text-align:center;padding-top:56px}
.member-hover b{display:block;font-size:13px;font-weight:600}
.member-hover small{font-size:9.5px}

/* news */
.news-title{left:529px;top:1474px}
.news-card{position:absolute;top:1551px;width:249px;height:375px;background:var(--card)}
.news-card.featured{background:var(--white);box-shadow:0 0 8px rgba(0,0,0,.18)}
.news-img{height:176px}
.news-body{padding:18px 21px}
.news-body h3{font-size:13px;font-weight:600;color:var(--blue);line-height:1.35}
.news-meta{font-size:9.5px;color:var(--orange);margin:8px 0 10px}
.news-body p{font-size:10.5px;line-height:1.45;color:var(--muted)}
.read-more{display:block;margin-top:14px;font-size:10.5px;color:var(--green)}

/* membership */
.membership{position:absolute;left:0;top:1998px;width:1200px;height:173px;background:linear-gradient(90deg,#eea41c,#f3b02c 50%,#eda21a)}
.membership h2{position:absolute;left:0;width:1200px;top:33px;text-align:center;color:var(--white);font-size:21px;font-weight:600}
.membership p{position:absolute;left:0;width:1200px;top:62px;text-align:center;color:var(--white);font-size:13px}
.field{position:absolute;top:102px;height:29px;border:1px solid rgba(255,255,255,.8);color:var(--white);font-size:10px;padding:7px 10px}
.send{position:absolute;left:839px;top:102px;width:85px;height:29px;background:var(--blue);color:var(--white);font-size:12px;text-align:center;line-height:29px}

/* footer */
.footer{position:absolute;left:0;top:2171px;width:610px;height:419px;background:var(--dark);color:var(--white)}
.footer-title{color:var(--white);left:207px;top:62px}
.footer-title .frame{border-color:#4a4647;left:44px}
.contact-list{position:absolute;left:207px;top:126px;font-size:11.5px;line-height:1.4}
.contact-list dt{font-weight:700;margin-top:8px}
.contact-list dt:first-child{margin-top:0}
.socials{position:absolute;left:207px;top:335px;display:flex;gap:6px}
.socials span{width:16px;height:16px;border-radius:50%;background:#6d7a8c}
.copyright{position:absolute;left:207px;top:369px;font-size:11px;color:#d0d0d0}
.copyright span{color:var(--green)}
.map{position:absolute;left:610px;top:2171px;width:590px;height:419px;background:linear-gradient(135deg,#e7ecd8 0%,#dfe7cf 45%,#a9cff2 65%,#8fc2f0 100%)}
</style>
</head>
<body>

<header class="site-header">
  <div class="brand"><span class="brand-dot"></span>VelLorim</div>
  <div class="top-contact">
    <span><svg width="11" height="11" viewBox="0 0 24 24"><path fill="#7cc142" d="M6.6 10.8a15 15 0 0 0 6.6 6.6l2.2-2.2c.3-.3.7-.4 1-.2 1.1.4 2.3.6 3.6.6.6 0 1 .4 1 1V20c0 .6-.4 1-1 1A17 17 0 0 1 3 4c0-.6.4-1 1-1h3.5c.6 0 1 .4 1 1 0 1.3.2 2.5.6 3.6.1.3 0 .7-.2 1z"/></svg>USA &nbsp;(+1) 555.210.4400 &nbsp;/&nbsp; UY &nbsp;(+598) 555.0183.62</span>
    <span><svg width="12" height="10" viewBox="0 0 24 18"><rect width="24" height="18" rx="2" fill="#7cc142"/><path d="M1 2l11 8 11-8" stroke="#fff" stroke-width="2" fill="none"/></svg>hello@vellorim-mail.com</span>
  </div>
  <nav class="main-nav">
    <a class="active">Home</a><a>About</a><a>Members Only</a><a>Team</a><a>News</a><a>Contact</a>
    <a class="btn-member">Become A Member</a>
  </nav>
</header>

<section class="hero">
  <div class="hero-photo" role="img" aria-label="Bottle of hemp oil with bowls of hemp seed and powder on a wooden table"></div>
  <h1 class="hero-title">VelLorim best <span>CBD-oil manufacturer</span></h1>
  <p class="hero-sub">Our hemp was enginnered to maximize therapeutic CBD. Under Uruguyan laws we refine the oil at 2x higher profitability than anywhere else in the world.</p>
  <div class="hero-btn">Discover More</div>
  <div class="arrow-btn" style="left:157px;top:188px;background:var(--blue)"><svg width="12" height="8" viewBox="0 0 12 8"><path d="M12 4H2M5 1L2 4l3 3" stroke="#fff" stroke-width="1.6" fill="none"/></svg></div>
  <div class="arrow-btn" style="left:1034px;top:188px;background:var(--orange)"><svg width="12" height="8" viewBox="0 0 12 8"><path d="M0 4h10M7 1l3 3-3 3" stroke="#fff" stroke-width="1.6" fill="none"/></svg></div>
</section>

<section class="about">
  <h2 class="sec-title" style="left:207px;top:572px"><span class="frame"></span>About Us</h2>
  <div class="about-text">
    <p>Our hemp was enginnered to maximize therapeutic CBD. Under Uruguyan laws we refine the oil at 2x higher profitability than anywhere else in the world.</p>
    <p>Lorem Ipsum is simply dummy text of the printing and typesetting industry. Lorem Ipsum has been the industry's standard dummy text ever since the 1500s, when an unknown printer took a galley of type and scrambled it to make a type specimen book. It has survived not only five centuries, but also the leap into electronic typesetting, remaining essentially.</p>
    <p>Our hemp was enginnered to maximize therapeutic CBD. Under Uruguyan laws we refine the oil at 2x higher profitability than anywhere else in the world.</p>
  </div>
  <div class="btn-orange" style="left:207px;top:911px;width:118px;height:29px;line-height:29px">Explore More &#9656;</div>

  <svg class="process-map" width="380" height="380" viewBox="-190 -190 380 380" font-family="Open Sans, Arial, sans-serif" font-size="12" text-anchor="middle">
    <g stroke="#c9c9c9" stroke-width="2" stroke-dasharray="4 4">
      <line x1="0" y1="0" x2="0" y2="-140"/>
      <line x1="0" y1="0" x2="121" y2="-70"/>
      <line x1="0" y1="0" x2="121" y2="70"/>
      <line x1="0" y1="0" x2="0" y2="140"/>
      <line x1="0" y1="0" x2="-121" y2="70"/>
      <line x1="0" y1="0" x2="-121" y2="-70"/>
    </g>
    <circle r="58" fill="#fff" stroke="#f0a51c" stroke-width="3"/>
    <circle r="48" fill="#f0a51c"/>
    <text y="7" font-size="20" fill="#fff">CBD</text>
    <g fill="#fff">
      <rect x="-58" y="-162" width="116" height="44" rx="4" fill="#1d5fb0"/>
      <text x="0" y="-143">Hemp</text><text x="0" y="-128">Cultivation</text>
      <rect x="63" y="-92" width="116" height="44" rx="4" fill="#3f9a8a"/>
      <text x="121" y="-66">Extraction</text>
      <rect x="63" y="48" width="116" height="44" rx="4" fill="#1d5fb0"/>
      <text x="121" y="67">Oil</text><text x="121" y="82">Refinement</text>
      <rect x="-58" y="118" width="116" height="44" rx="4" fill="#3f9a8a"/>
      <text x="0" y="137">Therapeutic</text><text x="0" y="152">Products</text>
      <rect x="-179" y="48" width="116" height="44" rx="4" fill="#1d5fb0"/>
      <text x="-121" y="67">New</text><text x="-121" y="82">Markets</text>
      <rect x="-179" y="-92" width="116" height="44" rx="4" fill="#3f9a8a"/>
      <text x="-121" y="-73">Genetic</text><text x="-121" y="-58">Engineering</text>
    </g>
  </svg>
</section>

<section class="team">
  <div class="team-watermark">MEMBERS</div>
  <h2 class="sec-title team-title"><span class="frame"></span>Our Team</h2>
  <p class="team-text">Our team is composed of experts, each an authority in their field. And each of us has a successful record of starting business.</p>
  <div class="team-rule"></div>
  <div class="member" style="left:478px;top:42px;background:linear-gradient(160deg,#7b6a5c,#4e4038)" role="img" aria-label="Portrait of a team member"></div>
  <div class="member" style="left:656px;top:42px;background:linear-gradient(160deg,#8a8f86,#5d6258)" role="img" aria-label="Portrait of a team member">
    <div class="member-hover"><b>Daniel Morrow</b><small>Business Development</small></div>
  </div>
  <div class="member" style="left:834px;top:42px;background:linear-gradient(160deg,#6d5e4e,#2b2622)" role="img" aria-label="Portrait of a team member"></div>
  <div class="member" style="left:478px;top:213px;background:linear-gradient(160deg,#8d8a86,#4d4f58)" role="img" aria-label="Portrait of a team member"></div>
  <div class="member" style="left:656px;top:213px;background:linear-gradient(160deg,#6f7a58,#3a3e33)" role="img" aria-label="Portrait of a team member"></div>
  <div class="member" style="left:834px;top:213px;background:linear-gradient(160deg,#6a5d4f,#2a2420)" role="img" aria-label="Portrait of a team member"></div>
</section>

<section class="news">
  <h2 class="sec-title news-title"><span class="frame" style="left:36px"></span>Our News</h2>
  <div class="arrow-btn" style="left:158px;top:1730px;background:#666"><svg width="12" height="8" viewBox="0 0 12 8"><path d="M12 4H2M5 1L2 4l3 3" stroke="#fff" stroke-width="1.6" fill="none"/></svg></div>
  <div class="arrow-btn" style="left:1034px;top:1730px;background:var(--orange)"><svg width="12" height="8" viewBox="0 0 12 8"><path d="M0 4h10M7 1l3 3-3 3" stroke="#fff" stroke-width="1.6" fill="none"/></svg></div>

  <article class="news-card featured" style="left:207px">
    <div class="news-img" style="background:linear-gradient(180deg,#f2f2f2,#d9d4cc)" role="img" aria-label="Woman holding a tablet against a white wall"></div>
    <div class="news-body">
      <h3>Lorem Ipsum is simply dummy text of the printing</h3>
      <div class="news-meta">March 8, 2016 &nbsp;&#9675; 0 Comments</div>
      <p>Lorem ipsum dolor sit amet, consectetuer adipiscing elit, sed diam nonummy nibh dolor sit amet, consectetuer adipiscing elit.....</p>
      <span class="read-more">Read More &#9656;</span>
    </div>
  </article>
  <article class="news-card" style="left:477px">
    <div class="news-img" style="background:linear-gradient(160deg,#a56a4e,#c9c6c0 60%,#8d8a86)" role="img" aria-label="Man with a tablet in an office"></div>
    <div class="news-body">
      <h3>Lorem Ipsum is simply dummy text of the printing</h3>
      <div class="news-meta">March 8, 2016 &nbsp;&#9675; 0 Comments</div>
      <p>Lorem ipsum dolor sit amet, consectetuer adipiscing elit, sed diam nonummy nibh dolor sit amet, consectetuer elit.....</p>
      <span class="read-more">Read More &#9656;</span>
    </div>
  </article>
  <article class="news-card" style="left:744px">
    <div class="news-img" style="background:linear-gradient(160deg,#c8c0b4,#5c6a7a 60%,#8f8676)" role="img" aria-label="Man in a suit reading a tablet on a sofa"></div>
    <div class="news-body">
      <h3>Lorem Ipsum is simply dummy text of the printing</h3>
      <div class="news-meta">March 8, 2016 &nbsp;&#9675; 0 Comments</div>
      <p>Lorem ipsum dolor sit amet, consectetuer adipiscing elit, sed diam nonummy nibh dolor sit amet, consectetuer .....</p>
      <span class="read-more">Read More &#9656;</span>
    </div>
  </article>
</section>

<section class="membership">
  <h2>Get A Membership</h2>
  <p>Potential investors between $30,000-$1,000,000 USD?</p>
  <div class="field" style="left:276px;width:259px">Name :</div>
  <div class="field" style="left:556px;width:261px">Enter Your Email :</div>
  <div class="send">Send</div>
</section>

<footer class="footer">
  <h2 class="sec-title footer-title"><span class="frame"></span>Contact Us</h2>
  <dl class="contact-list">
    <dt>Location:</dt><dd>Montevideo, Uruguay</dd>
    <dt>Call Us:</dt><dd>USA &nbsp;(+1) 555.210.4400<br>UY &nbsp;&nbsp;(+598) 555.0183.62</dd>
    <dt>Email:</dt><dd>info@vellorim-mail.com</dd>
    <dt>Website:</dt><dd>www.vellorim-hemp.uy</dd>
  </dl>
  <div class="socials"><span></span><span></span><span></span><span></span></div>
  <p class="copyright">Copyright &copy; 2017 <span>VelLorim</span>. &nbsp;All Rights Reserved.</p>
</footer>
<div class="map" role="img" aria-label="Road map of Uruguay and the Río de la Plata with a marker on Montevideo"></div>

</body>
</html>
```